Quotation (Proposal) Form

We are looking for a redesign of an existing form - one that fits our new marketing material better and, frankly, a form that looks a lot nicer than the boring form we use today. 8.5"x11". CMYK. Minimum 300 dpi necessary for printing. I have attached our current quote form as well as some other designs that show the direction we are going in. Please note, that this has to be able to have our people manually write in pen on it when we provide it to potential customers. Thank you!

Target Market(s)

Residential homeowners

Industry/Entity Type

Snow Removal

Font styles to use
Sans Serif

Colors

Designer to choose colors to be used in the design.

Requirements
Must have
• Should be easy to read and look great. Should also add the following text - "Exclusively serving Northeast Lakeview and suburbs"
Nice to have
• Similar concept to other marketing material we have done (attached). Easy to read. Professional.
Should not have
• Cluttered look. Unevenly spaced.

```html
<!DOCTYPE html>
<html lang="en">
<head>
<meta charset="utf-8">
<title>Maple Ridge Snowplowing – Seasonal Quote Form</title>
<link href="https://fonts.googleapis.com/css2?family=Didact+Gothic&family=Signika:wght@600;700&display=swap" rel="stylesheet">
<style>
  :root{
    --stage:#555555;
    --blue:#2a84c6;
    --blue-deep:#1d5f96;
    --white:#ffffff;
    --ink:#1b1b1b;
    --badge:#a3a3a3;
    --body-font:"Didact Gothic", sans-serif;
    --head-font:"Signika", sans-serif;
  }
  *{margin:0;padding:0;box-sizing:border-box}
  html,body{width:1200px;height:1200px;overflow:hidden;background:var(--stage)}
  .sheet{position:absolute;left:219px;top:92px;width:754px;height:976px;background:var(--white);font-family:var(--body-font);color:var(--ink)}
  .band{position:absolute;left:0;width:100%;background:var(--blue)}
  .band--top{top:0;height:26px}
  .band--main{top:166px;height:692px}
  .band--foot{top:960px;height:16px}
  .service-area{position:absolute;left:0;top:0;width:100%;height:26px;text-align:center;font-family:var(--head-font);font-weight:600;font-size:14px;line-height:26px;color:var(--white);letter-spacing:.4px}

  .brand{position:absolute;left:50px;top:46px;width:190px;text-align:center;font-family:var(--body-font);color:var(--ink)}
  .brand__mark{display:block;width:34px;height:34px;border-radius:50%;background:var(--blue);margin:0 auto 8px}
  .brand__name{font-size:28px;line-height:31px;display:block}

  .contact{position:absolute;left:407px;font-size:21px;line-height:23px;word-spacing:-2px}
  .contact svg{position:absolute;left:0}
  .contact span{position:absolute;left:24px;white-space:nowrap}
  .contact--addr{top:41px}
  .contact--phone{top:98px}
  .contact--phone span{font-family:var(--head-font);font-weight:700;font-size:25px;letter-spacing:.6px;word-spacing:0}
  .contact--mail{top:131px}

  .client{position:absolute;left:45px;top:178px;width:412px;height:160px;background:var(--white);border-radius:8px}
  .client__row{position:absolute;left:16px;right:42px;display:flex;align-items:flex-end;font-family:var(--head-font);font-weight:600;font-size:16px;height:19px}
  .client__row i{flex:1;border-bottom:1px solid var(--ink);margin-left:2px;margin-bottom:3px}

  .badge{position:absolute;width:64px;height:64px;border-radius:50%;background:var(--badge)}

  .quote{position:absolute;left:45px;top:374px;width:664px;height:468px;border:3px solid var(--white);border-radius:10px}
  .quote__tab{position:absolute;left:209px;top:354px;width:328px;height:44px;background:var(--white);border-radius:6px;text-align:center;font-family:var(--head-font);font-weight:700;font-size:41px;line-height:46px;color:var(--blue-deep);letter-spacing:.5px}
  .quote__title{position:absolute;left:63px;top:400px;font-family:var(--head-font);font-weight:600;font-size:24px;color:var(--white)}
  .terms{position:absolute;left:71px;top:0;width:620px;list-style:none;color:var(--white);font-size:15.6px;line-height:17px;word-spacing:-1px}
  .terms li{position:absolute;left:0;padding-left:24px;white-space:nowrap}
  .terms li svg{position:absolute;left:0;top:1px}
  .pay{position:absolute;right:215px;color:var(--white);font-size:15.6px;white-space:nowrap;word-spacing:-1px}
  .pay__box{position:absolute;left:549px;width:139px;height:25px;background:var(--white);border-radius:5px;font-family:var(--head-font);font-weight:600;font-size:16px;line-height:25px;padding-left:8px}

  .sign{position:absolute;left:113px;top:872px;width:528px;height:78px;border:2.5px solid var(--blue);border-radius:8px}
  .sign__legend{position:absolute;left:0;right:0;top:-12px;text-align:center}
  .sign__legend span{background:var(--white);padding:0 8px;font-family:var(--head-font);font-weight:600;font-size:16px;color:var(--blue)}
  .sign__row{position:absolute;left:26px;right:28px;display:flex;align-items:flex-end;font-family:var(--head-font);font-weight:600;font-size:16px;height:19px}
  .sign__row i{border-bottom:1px solid var(--ink);margin-bottom:3px;margin-left:2px}
</style>
</head>
<body>
<div class="sheet">
  <div class="band band--top"></div>
  <div class="service-area">Exclusively serving Northeast Lakeview and suburbs</div>

  <div class="brand">
    <span class="brand__mark"></span>
    <span class="brand__name">Maple Ridge</span>
    <span class="brand__name">Snowplowing</span>
  </div>

  <div class="contact contact--addr">
    <svg width="16" height="20" viewBox="0 0 16 20"><path d="M8 0a7 7 0 0 0-7 7c0 5 7 13 7 13s7-8 7-13a7 7 0 0 0-7-7zm0 10a3 3 0 1 1 0-6 3 3 0 0 1 0 6z" fill="#2a84c6"/></svg>
    <span>4180 Cedar Hollow Road NE</span>
    <span style="top:23px">Lakeview, MI 49500</span>
  </div>
  <div class="contact contact--phone">
    <svg width="20" height="20" viewBox="0 0 20 20" style="top:4px"><circle cx="10" cy="10" r="8.5" fill="none" stroke="#2a84c6" stroke-width="1.6"/><path d="M7 5.5l1.5 2.2-1 1.2c.6 1.4 1.6 2.4 3 3l1.2-1 2.2 1.5-.8 1.6c-3.6-.4-6.3-3.1-6.7-6.7z" fill="#2a84c6"/></svg>
    <span>(555) 014-2290</span>
  </div>
  <div class="contact contact--mail">
    <svg width="19" height="14" viewBox="0 0 19 14" style="top:5px"><rect x="0" y="0" width="19" height="14" fill="#2a84c6"/><path d="M0 0l9.5 7L19 0" fill="none" stroke="#fff" stroke-width="1.4"/></svg>
    <span>office@mapleridgesnow.com</span>
  </div>

  <div class="band band--main"></div>

  <div class="client">
    <div class="client__row" style="top:8px">Name<i></i></div>
    <div class="client__row" style="top:38px">Address<i></i></div>
    <div class="client__row" style="top:67px">Phone<i></i></div>
    <div class="client__row" style="top:97px">City<i style="flex:1.7"></i><span style="margin-left:2px">Zip</span><i></i></div>
    <div class="client__row" style="top:126px">Email Address <i style="margin-left:5px"></i></div>
  </div>

  <div class="badge" role="img" aria-label="Service award badge" style="left:514px;top:178px"></div>
  <div class="badge" role="img" aria-label="Service award badge" style="left:606px;top:178px"></div>
  <div class="badge" role="img" aria-label="Service award badge" style="left:514px;top:268px"></div>
  <div class="badge" role="img" aria-label="Service award badge" style="left:606px;top:268px"></div>

  <div class="quote"></div>
  <div class="quote__tab">SNOWPLOWING</div>
  <div class="quote__title">Unlimited Plowing Seasonal Quote</div>

  <ul class="terms">
    <li style="top:440px"><svg width="16" height="15" viewBox="0 0 16 15"><path d="M1 8l5 5L15 1" fill="none" stroke="#fff" stroke-width="3"/></svg>Maple Ridge is a fully licensed and insured snow removal service.</li>
    <li style="top:471px"><svg width="16" height="15" viewBox="0 0 16 15"><path d="M1 8l5 5L15 1" fill="none" stroke="#fff" stroke-width="3"/></svg>Plowing will be done when snow has accumulated 1” or more.</li>
    <li style="top:501px"><svg width="16" height="15" viewBox="0 0 16 15"><path d="M1 8l5 5L15 1" fill="none" stroke="#fff" stroke-width="3"/></svg>24 hour phone availability during snow events.</li>
    <li style="top:532px"><svg width="16" height="15" viewBox="0 0 16 15"><path d="M1 8l5 5L15 1" fill="none" stroke="#fff" stroke-width="3"/></svg>Hard rubber plow edges protect concrete and pavement from&nbsp; scratches and<br>rust marks.</li>
    <li style="top:580px"><svg width="16" height="15" viewBox="0 0 16 15"><path d="M1 8l5 5L15 1" fill="none" stroke="#fff" stroke-width="3"/></svg>Snow will be removed by 6:00 AM depending upon time and amount.</li>
    <li style="top:610px"><svg width="16" height="15" viewBox="0 0 16 15"><path d="M1 8l5 5L15 1" fill="none" stroke="#fff" stroke-width="3"/></svg>Hand shoveling of walkways/front patios available.</li>
    <li style="top:641px"><svg width="16" height="15" viewBox="0 0 16 15"><path d="M1 8l5 5L15 1" fill="none" stroke="#fff" stroke-width="3"/></svg>Salting of driveways available.</li>
    <li style="top:672px"><svg width="16" height="15" viewBox="0 0 16 15"><path d="M1 8l5 5L15 1" fill="none" stroke="#fff" stroke-width="3"/></svg>We will return to clean the approach of your drive after the city plows&nbsp; your street.</li>
    <li style="top:703px"><svg width="16" height="15" viewBox="0 0 16 15"><path d="M1 8l5 5L15 1" fill="none" stroke="#fff" stroke-width="3"/></svg>A slip-free surface can’t be guaranteed.</li>
    <li style="top:731px"><svg width="16" height="15" viewBox="0 0 16 15"><path d="M1 8l5 5L15 1" fill="none" stroke="#fff" stroke-width="3"/></svg>Email-based snow event information and real time updates provided to customers</li>
  </ul>

  <div class="pay" style="top:771px">One payment due by October 31</div>
  <div class="pay__box" style="top:768px">$</div>
  <div class="pay" style="top:804px">Two equal installments due by October 31 &amp; December 31</div>
  <div class="pay__box" style="top:801px">$</div>

  <div class="sign">
    <div class="sign__legend"><span>Please sing and retirn copy with payment</span></div>
    <div class="sign__row" style="top:13px">Maple Ridge:&nbsp;<i style="width:218px"></i><span style="margin-left:2px">Date:&nbsp;</span><i style="flex:1"></i></div>
    <div class="sign__row" style="top:42px">customer:<i style="width:250px"></i><span style="margin-left:2px">Date:</span><i style="flex:1"></i></div>
  </div>

  <div class="band band--foot"></div>
</div>
</body>
</html>
```